PowerPoint template for my training workshop business

I would like to have a PowerPoint template created using my logo and palette materials created by Brindlework. I train and facilitate workshops using PowerPoint in both corporate and public settings.

I have attached the original design elements to this request.

```html
<!DOCTYPE html>
<html lang="en">
<head>
<meta charset="utf-8">
<title>Presentation Deck – Workshop Template</title>
<link rel="stylesheet" href="https://fonts.googleapis.com/css2?family=Cinzel:wght@400;600;700&family=Montserrat:wght@400;500;600;700;800&display=swap">
<style>
:root{
  --teal:#163f49;
  --teal-deep:#0f2f37;
  --gold:#f6b42a;
  --orange:#f39a1e;
  --plum:#6a1d4f;
  --ink:#2c2c2c;
  --muted:#6d6d6d;
  --paper:#ffffff;
  --stage:#e7e9eb;
  --line:#d9dde0;
}
*{margin:0;padding:0;box-sizing:border-box}
html,body{width:1200px;height:2302px;overflow:hidden}
body{background:var(--stage);font-family:"Montserrat",Arial,sans-serif;color:var(--ink);position:relative}

.deck-title{position:absolute;left:70px;top:182px;color:var(--teal);font-weight:800;font-size:64px;line-height:1;letter-spacing:-1px}
.deck-title span{display:block;color:#222;font-weight:500;font-size:60px;margin-left:126px;margin-top:4px;letter-spacing:0}

.hero-slide{position:absolute;left:561px;top:85px;width:471px;height:263px;overflow:hidden}

.slide{position:absolute;width:384px;height:216px;background:var(--paper);overflow:hidden}
.abs{position:absolute}
.photo{position:absolute}

.serif{font-family:"Cinzel",Georgia,serif}
.h-slide{position:absolute;font-family:"Cinzel",Georgia,serif;font-weight:700;color:var(--teal);font-size:16px;letter-spacing:.2px;line-height:1.05}
.bar{position:absolute;width:3px;background:var(--gold)}
.body{font-size:4.6px;line-height:1.55;color:#555;text-align:justify}
.body p+p{margin-top:5px}
.tiny{font-size:4.2px;line-height:1.5;color:#666}
.label{font-family:"Cinzel",Georgia,serif;font-weight:700;font-size:6.2px;color:var(--teal)}

.foot-left,.foot-right{position:absolute;bottom:6px;font-size:3.6px;letter-spacing:.8px;color:#888}
.foot-left{left:10px}
.foot-right{right:10px}

.brand{position:absolute;font-family:"Cinzel",Georgia,serif;font-weight:700;font-size:4.6px;color:var(--gold);letter-spacing:.3px;white-space:nowrap}
.brand.small{right:12px;top:9px}
.brand.large{font-size:10px}
.brand.mid{font-size:7.5px}
.brand.centered{left:0;right:0;text-align:center}

.title-main{font-family:"Cinzel",Georgia,serif;font-weight:700;color:#fff;text-align:center}
.title-sub{color:#fff;text-align:center;font-size:6px;letter-spacing:.4px}

.side-band{position:absolute;left:0;top:0;bottom:0;background:var(--teal)}
.side-word{position:absolute;font-family:"Cinzel",Georgia,serif;font-weight:700;color:var(--gold);transform:rotate(-90deg);transform-origin:left top;white-space:nowrap}

.icon-circle{position:absolute;width:24px;height:24px;border-radius:50%;background:linear-gradient(160deg,var(--gold),var(--orange))}

.num-dot{position:absolute;width:14px;height:14px;border-radius:50%;background:var(--plum);color:#fff;font-size:4.5px;font-weight:700;display:flex;align-items:center;justify-content:center;border:1.5px solid #f1d7e6}
.card{position:absolute;background:#fff;border:1px solid #e3e3e3;border-radius:4px;box-shadow:0 2px 4px rgba(0,0,0,.08);padding:8px}
.card ul{list-style:none;margin-top:6px}
.card li{font-size:3.8px;color:#777;line-height:2.1}
.card li::before{content:"▸ ";color:var(--gold)}

.break-title{position:absolute;right:18px;font-family:"Cinzel",Georgia,serif;font-weight:700;color:#fff;font-size:15.5px;letter-spacing:.5px}
.break-rule{position:absolute;height:1px;background:rgba(255,255,255,.75)}
.break-sub{position:absolute;right:18px;color:#fff;font-size:9px;letter-spacing:2.6px}
.break-url{position:absolute;bottom:6px;left:0;right:0;text-align:center;color:rgba(255,255,255,.8);font-size:3.6px}

.step{position:absolute;height:14px}
.quote-box{position:absolute;background:#fff;border-radius:6px;padding:6px;font-size:3.8px;line-height:1.5;color:#666}
</style>
</head>
<body>

<h1 class="deck-title">Presentation<span>Deck</span></h1>

<!-- Hero title slide -->
<section class="hero-slide">
  <div class="photo" role="img" aria-label="Lake between mountains with a person sitting at the end of a wooden pier" style="inset:0;background:linear-gradient(180deg,#3a4f4f 0%,#2c4040 45%,#4d6462 60%,#263634 100%)"></div>
  <div class="brand large centered" style="top:106px">MAREN HOLT</div>
  <div class="title-main abs" style="left:0;right:0;top:132px;font-size:19px">PRESENTATION TITLE</div>
  <div class="title-sub abs" style="left:0;right:0;top:156px;font-size:8px">SUB TITLE GOES HERE</div>
</section>

<!-- Row 1 -->
<section class="slide" style="left:16px;top:492px">
  <div class="photo" role="img" aria-label="Lake between mountains with a person sitting at the end of a wooden pier" style="inset:0;background:linear-gradient(180deg,#3a4f4f 0%,#2c4040 45%,#4d6462 60%,#263634 100%)"></div>
  <div class="brand mid centered" style="top:80px">MAREN HOLT</div>
  <div class="title-main abs" style="left:0;right:0;top:97px;font-size:15px">PRESENTATION TITLE</div>
  <div class="title-sub abs" style="left:0;right:0;top:117px">SUB TITLE GOES HERE</div>
</section>

<section class="slide" style="left:408px;top:492px">
  <div class="side-band" style="width:75px"></div>
  <div class="side-word" style="left:28px;top:170px;font-size:22px">WELCOME</div>
  <div class="photo" role="img" aria-label="Two colleagues working together at a laptop" style="left:75px;top:0;width:153px;height:216px;background:linear-gradient(135deg,#b7a795,#6f5a4a 55%,#3b3530)"></div>
  <div class="brand small">MAREN HOLT</div>
  <div class="body abs" style="left:247px;top:50px;width:118px">
    <p>Plan each session with care so every group leaves with clear next steps. Short, focused exercises help teams turn new ideas into habits that last.</p>
    <p>Plan each session with care so every group leaves with clear next steps. Short, focused exercises help teams turn new ideas into habits that last.</p>
  </div>
  <div class="foot-right">PAGE | 1</div>
</section>

<section class="slide" style="left:800px;top:492px">
  <div class="side-band" style="width:53px"></div>
  <div class="side-word" style="left:16px;top:170px;font-size:19px">PART ONE</div>
  <div class="abs" style="left:170px;top:10px;width:28px;height:24px;background:var(--gold);color:#fff;font-weight:700;font-size:14px;display:flex;align-items:center;justify-content:center">01</div>
  <div class="h-slide" style="left:70px;top:52px">PICTURE<br>AND TEXT</div>
  <div class="body abs" style="left:70px;top:96px;width:118px">Plan each session with care so every group leaves with clear next steps. Short, focused exercises help teams turn new ideas into habits. Plan each session with care so every group leaves with clear next steps. Short, focused exercises help teams turn new ideas into habits that last.</div>
  <div class="photo" role="img" aria-label="Dark chair holding a lightbox sign" style="left:200px;top:0;width:184px;height:216px;background:linear-gradient(150deg,#cfcfcf,#8d8d8d 50%,#2e2e2e)"></div>
</section>

<!-- Row 2 -->
<section class="slide" style="left:16px;top:716px">
  <svg class="abs" style="left:0;top:0" width="384" height="110" viewBox="0 0 384 110"><path d="M0 0H384V78Q384 92 370 92H330Q314 92 306 104Q300 110 290 110H0Z" fill="var(--teal)"/></svg>
  <div class="serif abs" style="left:105px;top:24px;color:var(--gold);font-weight:700;font-size:21px">MAREN HOLT</div>
  <div class="abs" style="left:155px;top:52px;color:#fff;font-size:9px">Add title here</div>
  <div class="abs" style="left:180px;top:67px;display:flex;gap:2px"><span style="width:5px;height:5px;border-radius:50%;background:#fff"></span><span style="width:5px;height:5px;border-radius:50%;background:#fff"></span><span style="width:5px;height:5px;border-radius:50%;background:#fff"></span></div>
  <div class="photo" role="img" aria-label="Portrait of the coach" style="left:285px;top:62px;width:64px;height:64px;border-radius:50%;border:2px solid #fff;background:radial-gradient(circle at 50% 40%,#d9b89a,#9a7657 60%,#5a5a4a)"></div>
  <div class="serif abs" style="left:16px;top:124px;font-size:9px;color:#555">MAREN HOLT</div>
  <div class="body abs" style="left:16px;top:138px;width:235px">Plan each session with care so every group leaves with clear next steps. Short, focused exercises help teams turn new ideas into habits. Plan each session with care so every group leaves with clear next steps and real results.</div>
  <div class="abs" style="left:260px;top:146px;font-size:6px;color:var(--teal);line-height:1.9">✉ hello@marenholt.example<br>☎ 0044 700 000 1234</div>
  <div class="foot-right">4</div>
</section>

<section class="slide" style="left:408px;top:716px">
  <div class="abs" style="left:47px;top:42px;width:104px;height:106px;border-radius:8px;background:var(--teal)"></div>
  <div class="photo" role="img" aria-label="Portrait of the coach" style="left:48px;top:42px;width:102px;height:104px;border-radius:8px;background:linear-gradient(160deg,#cdb59b,#8e7560 60%,#4e4a3a)"></div>
  <div class="abs" style="left:48px;top:132px;width:76px;height:14px;background:var(--teal);border-radius:0 0 0 8px;color:#fff;font-family:Cinzel,serif;font-size:5.5px;display:flex;align-items:center;justify-content:center">YOUR NAME</div>
  <div class="h-slide" style="left:185px;top:30px">WELCOME MESSAGE</div>
  <div class="abs serif" style="left:180px;top:62px;font-size:22px;color:#bbb">“</div>
  <div class="body abs" style="left:192px;top:72px;width:172px">
    <p>Plan each session with care so every group leaves with clear next steps. Short, focused exercises help teams turn new ideas into habits.</p>
    <p>Plan each session with care so every group leaves with clear next steps. Short, focused exercises help teams turn new ideas into habits. Plan each session with care so every group leaves with clear next steps and results.</p>
  </div>
  <div class="brand small">MAREN HOLT</div>
  <div class="foot-left">COPYRIGHT © 2020</div><div class="foot-right">PAGE | 5</div>
</section>

<section class="slide" style="left:800px;top:716px">
  <div class="h-slide" style="left:26px;top:82px;font-size:16.5px">MISSION,<br>VISION &amp;<br>GOAL</div>
  <svg class="abs" style="left:196px;top:34px" width="26" height="18" viewBox="0 0 26 18"><path d="M2 9L8 4L13 7L18 4L24 9L16 15L10 11" fill="none" stroke="#333" stroke-width="1.2"/></svg>
  <div class="label abs" style="left:234px;top:34px;font-size:5.5px">FREE INTRODUCTORY SESSION</div>
  <div class="tiny abs" style="left:234px;top:42px;width:135px">“Let us find out how a workshop can help meet your goals.”</div>
  <div class="abs" style="left:178px;top:74px;width:206px;height:74px;border-radius:8px 0 0 8px;background:linear-gradient(135deg,var(--orange),var(--gold));box-shadow:0 3px 6px rgba(0,0,0,.12)"></div>
  <svg class="abs" style="left:198px;top:100px" width="22" height="16" viewBox="0 0 22 16"><circle cx="6" cy="10" r="4.5" fill="none" stroke="#fff" stroke-width="1.4"/><circle cx="16" cy="10" r="4.5" fill="none" stroke="#fff" stroke-width="1.4"/><path d="M6 5L9 2M16 5L13 2" stroke="#fff" stroke-width="1.4"/></svg>
  <div class="label abs" style="left:234px;top:96px;font-size:5.5px;color:#fff">DISCOVERY SESSION</div>
  <div class="tiny abs" style="left:234px;top:104px;width:135px;color:#fff">“We get to know each other better and shape a plan that helps you meet your goals.”</div>
  <svg class="abs" style="left:200px;top:162px" width="20" height="20" viewBox="0 0 20 20"><path d="M2 18H18M5 18V13H9V18M11 18V9H15V18M7 10V4M7 4L12 4" fill="none" stroke="#333" stroke-width="1.2"/></svg>
  <div class="label abs" style="left:234px;top:162px;font-size:5.5px">COACHING<br>SESSION</div>
  <div class="tiny abs" style="left:234px;top:176px;width:135px">“A steady coaching rhythm helps you keep working toward your goals.”</div>
  <div class="brand small">MAREN HOLT</div>
  <div class="foot-left">COPYRIGHT © 2020</div><div class="foot-right">PAGE | 6</div>
</section>

<!-- Row 3 -->
<section class="slide" style="left:16px;top:940px">
  <div class="bar" style="left:24px;top:28px;height:32px"></div>
  <div class="h-slide" style="left:36px;top:38px;font-size:17px">OVERVIEW</div>
  <div class="body abs" style="left:24px;top:80px;width:336px;font-size:4.2px">
    <p>Plan each session with care so every group leaves with clear next steps. Short, focused exercises help teams turn new ideas into habits. Plan each session with care so every group leaves with clear next steps. Short, focused exercises help teams turn new ideas into habits.</p>
    <p>Plan each session with care so every group leaves with clear next steps. Short, focused exercises help teams turn new ideas into habits. Plan each session with care so every group leaves with clear next steps. Short, focused exercises help teams turn new ideas into habits.</p>
    <p>Plan each session with care so every group leaves with clear next steps. Short, focused exercises help teams turn new ideas into habits. Plan each session with care so every group leaves with clear next steps. Short, focused exercises help teams turn new ideas into habits. Plan each session with care so every group leaves with clear next steps.</p>
  </div>
  <div class="brand small">MAREN HOLT</div>
  <div class="foot-left">COPYRIGHT © 2020</div><div class="foot-right">PAGE | 7</div>
</section>

<section class="slide" style="left:408px;top:940px">
  <div class="bar" style="left:14px;top:20px;height:28px"></div>
  <div class="h-slide" style="left:26px;top:28px">FOUR POINTS</div>
  <svg class="abs" style="left:0;top:80px" width="384" height="96" viewBox="0 0 384 96">
    <circle cx="76" cy="48" r="38" fill="none" stroke="var(--plum)" stroke-width="8"/>
    <circle cx="152" cy="48" r="38" fill="none" stroke="var(--teal)" stroke-width="8"/>
    <circle cx="228" cy="48" r="38" fill="none" stroke="var(--plum)" stroke-width="8"/>
    <circle cx="304" cy="48" r="38" fill="none" stroke="var(--teal)" stroke-width="8"/>
  </svg>
  <div class="tiny abs" style="left:52px;top:110px;width:48px;text-align:center">Short exercises help teams turn ideas into habits.</div>
  <div class="tiny abs" style="left:128px;top:110px;width:48px;text-align:center">Short exercises help teams turn ideas into habits.</div>
  <div class="tiny abs" style="left:204px;top:110px;width:48px;text-align:center">Short exercises help teams turn ideas into habits.</div>
  <div class="tiny abs" style="left:280px;top:110px;width:48px;text-align:center">Short exercises help teams turn ideas into habits.</div>
  <div class="brand small">MAREN HOLT</div>
  <div class="foot-left">COPYRIGHT © 2020</div><div class="foot-right">PAGE | 8</div>
</section>

<section class="slide" style="left:800px;top:940px">
  <div class="serif abs" style="left:42px;top:38px;font-size:8.5px;font-weight:700;color:var(--teal);line-height:1.35">SUCCESS IS NOT ONLY WHAT<br>YOU ACHIEVE IN YOUR LIFE,<br>BUT ALSO WHAT YOU INSPIRE<br>IN THE LIVES OF OTHERS</div>
  <div class="photo" role="img" aria-label="Person silhouetted against a golden sunset" style="left:0;top:108px;width:384px;height:108px;background:linear-gradient(180deg,#f8d98a 0%,#f3b43b 45%,#ee9a1c 100%)"></div>
  <div class="label abs" style="left:40px;top:137px;color:var(--teal)">LOREM IPSUM DOLOR</div>
  <div class="label abs" style="left:153px;top:137px;color:var(--teal)">LOREM IPSUM DOLOR</div>
  <div class="label abs" style="left:262px;top:137px;color:var(--teal)">LOREM IPSUM DOLOR</div>
  <div class="tiny abs" style="left:40px;top:152px;width:95px;color:#fff">Short, focused exercises help teams turn new ideas into habits.</div>
  <div class="tiny abs" style="left:153px;top:152px;width:95px;color:#fff">Short, focused exercises help teams turn new ideas into habits.</div>
  <div class="tiny abs" style="left:262px;top:152px;width:95px;color:#fff">Short, focused exercises help teams turn new ideas into habits.</div>
</section>

<!-- Row 4 -->
<section class="slide" style="left:16px;top:1164px">
  <div class="bar" style="left:14px;top:10px;height:26px"></div>
  <div class="h-slide" style="left:26px;top:18px">YOUR AWESOME TEXT</div>
  <div class="photo" role="img" aria-label="Forest path lit by morning sun" style="left:0;top:48px;width:384px;height:80px;background:linear-gradient(90deg,#2a2a1c,#6b5a2c 40%,#3d3a22)"></div>
  <div class="abs" style="left:192px;top:48px;width:192px;height:80px;background:var(--teal)"></div>
  <div class="body abs" style="left:202px;top:56px;width:172px;color:#fff">Plan each session with care so every group leaves with clear next steps. Short, focused exercises help teams turn new ideas into habits. Plan each session with care so every group leaves with clear steps.</div>
  <div class="body abs" style="left:18px;top:140px;width:160px">Plan each session with care so every group leaves with clear next steps. Short, focused exercises help teams turn new ideas into habits. Plan each session with care and results.</div>
  <div class="body abs" style="left:204px;top:140px;width:160px">Plan each session with care so every group leaves with clear next steps. Short, focused exercises help teams turn new ideas into habits. Plan each session with care and results.</div>
  <div class="brand small">MAREN HOLT</div>
  <div class="foot-left">COPYRIGHT © 2020</div><div class="foot-right">PAGE | 10</div>
</section>

<section class="slide" style="left:408px;top:1164px">
  <div class="bar" style="left:14px;top:20px;height:28px"></div>
  <div class="h-slide" style="left:30px;top:28px;font-size:15px">POSITIVE AND NEGATIVE</div>
  <div class="abs" style="left:30px;top:52px;width:320px;height:1px;background:var(--line)"></div>
  <div class="abs" style="left:162px;top:52px;width:46px;height:5px;background:var(--teal);border-radius:0 0 3px 3px"></div>
  <div class="abs" style="left:185px;top:57px;width:1px;height:140px;background:var(--line)"></div>
  <svg class="abs" style="left:44px;top:72px" width="14" height="106" viewBox="0 0 14 106">
    <g fill="var(--teal)"><circle cx="7" cy="7" r="6.5"/><circle cx="7" cy="37" r="6.5"/><circle cx="7" cy="67" r="6.5"/><circle cx="7" cy="97" r="6.5"/></g>
    <g fill="none" stroke="#fff" stroke-width="1.5"><path d="M4 7L6 9L10 5"/><path d="M4 37L6 39L10 35"/><path d="M4 67L6 69L10 65"/><path d="M4 97L6 99L10 95"/></g>
  </svg>
  <svg class="abs" style="left:216px;top:72px" width="14" height="106" viewBox="0 0 14 106">
    <g fill="#d32f2f"><circle cx="7" cy="7" r="6.5"/><circle cx="7" cy="37" r="6.5"/><circle cx="7" cy="67" r="6.5"/><circle cx="7" cy="97" r="6.5"/></g>
    <g stroke="#fff" stroke-width="1.5"><path d="M4.5 4.5L9.5 9.5M9.5 4.5L4.5 9.5"/><path d="M4.5 34.5L9.5 39.5M9.5 34.5L4.5 39.5"/><path d="M4.5 64.5L9.5 69.5M9.5 64.5L4.5 69.5"/><path d="M4.5 94.5L9.5 99.5M9.5 94.5L4.5 99.5"/></g>
  </svg>
  <div class="tiny abs" style="left:64px;top:72px;width:110px;line-height:1.55">Short, focused exercises help teams turn new ideas into habits that last.</div>
  <div class="tiny abs" style="left:64px;top:102px;width:110px;line-height:1.55">Short, focused exercises help teams turn new ideas into habits that last.</div>
  <div class="tiny abs" style="left:64px;top:132px;width:110px;line-height:1.55">Short, focused exercises help teams turn new ideas into habits that last.</div>
  <div class="tiny abs" style="left:64px;top:162px;width:110px;line-height:1.55">Short, focused exercises help teams turn new ideas into habits that last.</div>
  <div class="tiny abs" style="left:236px;top:72px;width:110px;line-height:1.55">Short, focused exercises help teams turn new ideas into habits that last.</div>
  <div class="tiny abs" style="left:236px;top:102px;width:110px;line-height:1.55">Short, focused exercises help teams turn new ideas into habits that last.</div>
  <div class="tiny abs" style="left:236px;top:132px;width:110px;line-height:1.55">Short, focused exercises help teams turn new ideas into habits that last.</div>
  <div class="tiny abs" style="left:236px;top:162px;width:110px;line-height:1.55">Short, focused exercises help teams turn new ideas into habits that last.</div>
  <div class="brand small">MAREN HOLT</div>
  <div class="foot-left">COPYRIGHT © 2020</div><div class="foot-right">PAGE | 11</div>
</section>

<section class="slide" style="left:800px;top:1164px">
  <div class="bar" style="left:20px;top:20px;height:28px"></div>
  <div class="h-slide" style="left:32px;top:28px">YOUR AWESOME TEXT</div>
  <div class="icon-circle" style="left:56px;top:66px"></div>
  <div class="icon-circle" style="left:176px;top:66px"></div>
  <div class="icon-circle" style="left:296px;top:66px"></div>
  <div class="tiny abs" style="left:20px;top:94px;width:96px;text-align:center">Short, focused exercises help teams turn new ideas into habits.</div>
  <div class="tiny abs" style="left:140px;top:94px;width:96px;text-align:center">Short, focused exercises help teams turn new ideas into habits.</div>
  <div class="tiny abs" style="left:260px;top:94px;width:96px;text-align:center">Short, focused exercises help teams turn new ideas into habits.</div>
  <div class="icon-circle" style="left:56px;top:138px"></div>
  <div class="icon-circle" style="left:176px;top:138px"></div>
  <div class="icon-circle" style="left:296px;top:138px"></div>
  <div class="tiny abs" style="left:20px;top:166px;width:96px;text-align:center">Short, focused exercises help teams turn new ideas into habits.</div>
  <div class="tiny abs" style="left:140px;top:166px;width:96px;text-align:center">Short, focused exercises help teams turn new ideas into habits.</div>
  <div class="tiny abs" style="left:260px;top:166px;width:96px;text-align:center">Short, focused exercises help teams turn new ideas into habits.</div>
  <div class="brand small">MAREN HOLT</div>
  <div class="foot-left">COPYRIGHT © 2020</div><div class="foot-right">PAGE | 12</div>
</section>

<!-- Row 5 -->
<section class="slide" style="left:16px;top:1389px">
  <div class="h-slide" style="left:20px;top:48px;width:96px;text-align:right;font-size:12.5px">YOUR<br>AWESOME<br>TEXT</div>
  <div class="bar" style="left:118px;top:58px;height:26px"></div>
  <div class="tiny abs" style="left:20px;top:94px;width:96px;text-align:right">Plan each session with care so every group leaves with clear next steps. Short, focused exercises help teams turn new ideas into habits that last.</div>
  <div class="num-dot" style="left:132px;top:52px">01</div>
  <div class="num-dot" style="left:132px;top:104px">02</div>
  <div class="num-dot" style="left:132px;top:156px">03</div>
  <div class="num-dot" style="left:257px;top:52px">04</div>
  <div class="num-dot" style="left:257px;top:104px">05</div>
  <div class="num-dot" style="left:257px;top:156px">06</div>
  <div class="abs" style="left:158px;top:46px;width:90px"><div class="label" style="font-size:5px">PROJECT NAME</div><div class="tiny">Short exercises help teams turn new ideas into habits.</div></div>
  <div class="abs" style="left:158px;top:98px;width:90px"><div class="label" style="font-size:5px">PROJECT NAME</div><div class="tiny">Short exercises help teams turn new ideas into habits.</div></div>
  <div class="abs" style="left:158px;top:150px;width:90px"><div class="label" style="font-size:5px">PROJECT NAME</div><div class="tiny">Short exercises help teams turn new ideas into habits.</div></div>
  <div class="abs" style="left:283px;top:46px;width:90px"><div class="label" style="font-size:5px">PROJECT NAME</div><div class="tiny">Short exercises help teams turn new ideas into habits.</div></div>
  <div class="abs" style="left:283px;top:98px;width:90px"><div class="label" style="font-size:5px">PROJECT NAME</div><div class="tiny">Short exercises help teams turn new ideas into habits.</div></div>
  <div class="abs" style="left:283px;top:150px;width:90px"><div class="label" style="font-size:5px">PROJECT NAME</div><div class="tiny">Short exercises help teams turn new ideas into habits.</div></div>
  <div class="brand small">MAREN HOLT</div>
  <div class="foot-left">COPYRIGHT © 2020</div><div class="foot-right">PAGE | 13</div>
</section>

<section class="slide" style="left:408px;top:1389px">
  <div class="bar" style="left:20px;top:20px;height:28px"></div>
  <div class="h-slide" style="left:33px;top:28px">PICTURES AND TEXT</div>
  <div class="photo" role="img" aria-label="Hiker sitting on a rock facing a warm sunset" style="left:30px;top:58px;width:88px;height:74px;background:linear-gradient(180deg,#f0d3b0,#c79470 60%,#6f5a52)"></div>
  <div class="serif abs" style="left:32px;top:170px;font-size:18px;color:var(--teal)">01</div>
  <div class="tiny abs" style="left:62px;top:172px;width:60px">Short exercises help teams turn new ideas into habits.</div>
  <div class="serif abs" style="left:142px;top:60px;font-size:18px;color:var(--teal)">02</div>
  <div class="tiny abs" style="left:172px;top:60px;width:60px">Short exercises help teams turn new ideas into habits.</div>
  <div class="photo" role="img" aria-label="Neon word sign on a leafy wall" style="left:142px;top:96px;width:86px;height:102px;background:linear-gradient(160deg,#2a3a26,#152012)"></div>
  <div class="photo" role="img" aria-label="Dark chair holding a lightbox sign" style="left:256px;top:58px;width:86px;height:74px;background:linear-gradient(150deg,#cfcfcf,#7a7a7a 55%,#2c2c2c)"></div>
  <div class="serif abs" style="left:256px;top:170px;font-size:18px;color:var(--teal)">03</div>
  <div class="tiny abs" style="left:284px;top:172px;width:60px">Short exercises help teams turn new ideas into habits.</div>
  <div class="brand small">MAREN HOLT</div>
  <div class="foot-left">COPYRIGHT © 2020</div><div class="foot-right">PAGE | 14</div>
</section>

<section class="slide" style="left:800px;top:1389px">
  <div class="bar" style="left:14px;top:20px;height:28px"></div>
  <div class="h-slide" style="left:27px;top:28px;font-size:15.5px">THREE COLUMN TEXT</div>
  <div class="abs" style="left:0;top:55px;width:384px;height:38px;background:#f3f3f3"></div>
  <div class="tiny abs" style="left:20px;top:66px;width:344px;text-align:center">Plan each session with care so every group leaves with clear next steps. Short, focused exercises help teams turn new ideas into habits that last for years.</div>
  <div class="card" style="left:15px;top:92px;width:110px;height:96px"><div class="label" style="font-size:5.6px">LOREM IPSUM DOLOR</div><div class="tiny">Short exercises help teams turn new ideas into habits.</div><ul><li>Set goals</li><li>Share ideas</li><li>Try it out</li><li>Reflect</li><li>Follow up</li></ul></div>
  <div class="card" style="left:136px;top:92px;width:110px;height:96px"><div class="label" style="font-size:5.6px">LOREM IPSUM DOLOR</div><div class="tiny">Short exercises help teams turn new ideas into habits.</div><ul><li>Set goals</li><li>Share ideas</li><li>Try it out</li><li>Reflect</li><li>Follow up</li></ul></div>
  <div class="card" style="left:258px;top:92px;width:110px;height:96px"><div class="label" style="font-size:5.6px">LOREM IPSUM DOLOR</div><div class="tiny">Short exercises help teams turn new ideas into habits.</div><ul><li>Set goals</li><li>Share ideas</li><li>Try it out</li><li>Reflect</li><li>Follow up</li></ul></div>
  <div class="brand small">MAREN HOLT</div>
  <div class="foot-left">COPYRIGHT © 2020</div><div class="foot-right">PAGE | 15</div>
</section>

<!-- Row 6 -->
<section class="slide" style="left:16px;top:1615px">
  <div class="h-slide" style="left:20px;top:70px">STEPS TO<br>SUCCESS</div>
  <div class="photo" role="img" aria-label="Figure climbing stairs" style="left:208px;top:24px;width:44px;height:62px;background:var(--orange);border-radius:6px 6px 2px 2px;opacity:.9"></div>
  <div class="step" style="left:14px;top:165px;width:60px;background:var(--plum)"></div>
  <div class="step" style="left:102px;top:140px;width:60px;background:var(--teal)"></div>
  <div class="step" style="left:172px;top:118px;width:62px;background:var(--teal)"></div>
  <div class="step" style="left:244px;top:92px;width:62px;background:var(--orange)"></div>
  <div class="step" style="left:312px;top:70px;width:62px;background:var(--orange)"></div>
  <div class="abs" style="left:14px;top:184px;width:80px"><div style="font-size:4.6px">Lorem ipsum dolor</div><div class="tiny">Short exercises help teams grow.</div></div>
  <div class="abs" style="left:102px;top:158px;width:64px"><div style="font-size:4.6px">Lorem ipsum dolor</div><div class="tiny">Short exercises help teams grow.</div></div>
  <div class="abs" style="left:172px;top:136px;width:64px"><div style="font-size:4.6px">Lorem ipsum dolor</div><div class="tiny">Short exercises help teams grow.</div></div>
  <div class="abs" style="left:244px;top:110px;width:64px"><div style="font-size:4.6px">Lorem ipsum dolor</div><div class="tiny">Short exercises help teams grow.</div></div>
  <div class="abs" style="left:312px;top:88px;width:64px"><div style="font-size:4.6px">Lorem ipsum dolor</div><div class="tiny">Short exercises help teams grow.</div></div>
  <div class="brand small">MAREN HOLT</div>
  <div class="foot-left">COPYRIGHT © 2020</div><div class="foot-right">PAGE | 16</div>
</section>

<section class="slide" style="left:408px;top:1615px">
  <div class="bar" style="left:14px;top:20px;height:28px"></div>
  <div class="h-slide" style="left:26px;top:28px;font-size:15.5px">CIRCLE INFOGRAPHIC</div>
  <svg class="abs" style="left:142px;top:74px" width="100" height="100" viewBox="0 0 100 100">
    <g fill="none" stroke-width="22" transform="rotate(-90 50 50)">
      <circle cx="50" cy="50" r="34" stroke="var(--plum)" stroke-dasharray="33.6 180" stroke-dashoffset="0"/>
      <circle cx="50" cy="50" r="34" stroke="var(--gold)" stroke-dasharray="33.6 180" stroke-dashoffset="-35.6"/>
      <circle cx="50" cy="50" r="34" stroke="var(--teal)" stroke-dasharray="33.6 180" stroke-dashoffset="-71.2"/>
      <circle cx="50" cy="50" r="34" stroke="var(--plum)" stroke-dasharray="33.6 180" stroke-dashoffset="-106.8"/>
      <circle cx="50" cy="50" r="34" stroke="var(--gold)" stroke-dasharray="33.6 180" stroke-dashoffset="-142.4"/>
      <circle cx="50" cy="50" r="34" stroke="var(--teal)" stroke-dasharray="33.6 180" stroke-dashoffset="-178"/>
    </g>
  </svg>
  <div class="abs" style="left:50px;top:62px;width:90px;text-align:right"><div class="label" style="font-size:5.4px">LOREM IPSUM DOLOR</div><div class="tiny">Short exercises help teams turn ideas into habits.</div></div>
  <div class="abs" style="left:30px;top:116px;width:90px;text-align:right"><div class="label" style="font-size:5.4px">LOREM IPSUM DOLOR</div><div class="tiny">Short exercises help teams turn ideas into habits.</div></div>
  <div class="abs" style="left:50px;top:168px;width:90px;text-align:right"><div class="label" style="font-size:5.4px">LOREM IPSUM DOLOR</div><div class="tiny">Short exercises help teams turn ideas into habits.</div></div>
  <div class="abs" style="left:244px;top:62px;width:90px"><div class="label" style="font-size:5.4px">LOREM IPSUM DOLOR</div><div class="tiny">Short exercises help teams turn ideas into habits.</div></div>
  <div class="abs" style="left:264px;top:116px;width:90px"><div class="label" style="font-size:5.4px">LOREM IPSUM DOLOR</div><div class="tiny">Short exercises help teams turn ideas into habits.</div></div>
  <div class="abs" style="left:244px;top:168px;width:90px"><div class="label" style="font-size:5.4px">LOREM IPSUM DOLOR</div><div class="tiny">Short exercises help teams turn ideas into habits.</div></div>
  <div class="brand small">MAREN HOLT</div>
  <div class="foot-left">COPYRIGHT © 2020</div><div class="foot-right">PAGE | 17</div>
</section>

<section class="slide" style="left:800px;top:1615px">
  <div class="bar" style="left:14px;top:20px;height:28px"></div>
  <div class="h-slide" style="left:28px;top:28px;font-size:15.5px">PYRAMID INFOGRAPHIC</div>
  <svg class="abs" style="left:30px;top:56px" width="110" height="130" viewBox="0 0 110 130">
    <defs><clipPath id="pyramid-face"><path d="M68 2L62 124L104 104Z"/></clipPath></defs>
    <path d="M68 2L6 110L62 124Z" fill="var(--teal)"/>
    <g clip-path="url(#pyramid-face)">
      <rect width="110" height="130" fill="var(--plum)"/>
      <rect y="22" width="110" height="14" fill="var(--gold)"/>
      <rect y="52" width="110" height="14" fill="var(--gold)"/>
      <rect y="82" width="110" height="14" fill="var(--gold)"/>
    </g>
    <path d="M68 2L62 124" stroke="#1d1d1d" stroke-width=".6"/>
  </svg>
  <svg class="abs" style="left:100px;top:60px" width="150" height="100" viewBox="0 0 150 100">
    <g stroke="var(--teal)" stroke-width="1"><path d="M20 4H138"/><path d="M32 34H138"/><path d="M42 63H138"/><path d="M52 92H138"/></g>
    <g fill="var(--teal)"><circle cx="138" cy="4" r="2"/><circle cx="138" cy="34" r="2"/><circle cx="138" cy="63" r="2"/><circle cx="138" cy="92" r="2"/></g>
  </svg>
  <div class="abs" style="left:243px;top:58px;width:125px"><div class="label" style="font-size:5.4px">LOREM IPSUM DOLOR</div><div class="tiny">Short exercises help teams turn ideas into habits.</div></div>
  <div class="abs" style="left:243px;top:88px;width:125px"><div class="label" style="font-size:5.4px">LOREM IPSUM DOLOR</div><div class="tiny">Short exercises help teams turn ideas into habits.</div></div>
  <div class="abs" style="left:243px;top:117px;width:125px"><div class="label" style="font-size:5.4px">LOREM IPSUM DOLOR</div><div class="tiny">Short exercises help teams turn ideas into habits.</div></div>
  <div class="abs" style="left:243px;top:147px;width:125px"><div class="label" style="font-size:5.4px">LOREM IPSUM DOLOR</div><div class="tiny">Short exercises help teams turn ideas into habits.</div></div>
  <div class="brand small">MAREN HOLT</div>
  <div class="foot-left">COPYRIGHT © 2020</div><div class="foot-right">PAGE | 18</div>
</section>

<!-- Row 7 -->
<section class="slide" style="left:16px;top:1840px">
  <div class="bar" style="left:18px;top:20px;height:28px"></div>
  <div class="h-slide" style="left:30px;top:28px;font-size:15.5px">THREE COLUMN TEXT</div>
  <div class="serif abs" style="left:30px;top:70px;font-size:18px;color:var(--teal)">01</div>
  <div class="tiny abs" style="left:64px;top:70px;width:240px">Plan each session with care so every group leaves with clear next steps. Short, focused exercises help teams turn new ideas into habits that last.</div>
  <div class="abs" style="left:62px;top:98px;width:250px;height:48px;background:var(--teal);border-radius:6px"></div>
  <div class="serif abs" style="left:30px;top:112px;font-size:18px;color:var(--teal)">02</div>
  <div class="tiny abs" style="left:70px;top:104px;width:200px;color:#fff">Plan each session with care so every group leaves with clear next steps. Short, focused exercises help teams turn new ideas into habits that last for years.</div>
  <div class="serif abs" style="left:30px;top:160px;font-size:18px;color:var(--teal)">03</div>
  <div class="tiny abs" style="left:64px;top:160px;width:240px">Plan each session with care so every group leaves with clear next steps. Short, focused exercises help teams turn new ideas into habits that last.</div>
  <svg class="abs" style="left:262px;top:78px" width="110" height="100" viewBox="0 0 110 100">
    <circle cx="42" cy="44" r="36" fill="var(--teal)"/>
    <circle cx="42" cy="44" r="26" fill="#fff"/>
    <path d="M68 70L92 94" stroke="var(--teal)" stroke-width="12" stroke-linecap="round"/>
    <rect x="39" y="28" width="6" height="20" rx="2" fill="var(--teal)"/>
    <circle cx="42" cy="56" r="3.4" fill="var(--teal)"/>
  </svg>
  <div class="brand small">MAREN HOLT</div>
  <div class="foot-left">COPYRIGHT © 2020</div><div class="foot-right">PAGE | 19</div>
</section>

<section class="slide" style="left:408px;top:1840px">
  <div class="abs" style="inset:0;background:var(--teal)"></div>
  <div class="photo" role="img" aria-label="Mosaic of mountain lake photos in diamond tiles" style="left:0;top:0;width:260px;height:216px;background:linear-gradient(160deg,#9fb3b0,#4f6f68 55%,#2f4a44);clip-path:polygon(0 0,100% 0,100% 62%,72% 100%,0 100%)"></div>
  <div class="abs" style="left:0;top:140px;width:384px;height:76px;background:#fff;clip-path:polygon(0 30%,60% 30%,70% 0,100% 0,100% 100%,0 100%)"></div>
  <div class="abs" style="left:214px;top:32px;color:#fff;font-size:6px;letter-spacing:1.6px">SUB TITLE GOES HERE</div>
  <div class="serif abs" style="left:224px;top:42px;color:#fff;font-size:15px;line-height:1.3">YOUR TEXT OR<br>QUOTE HERE</div>
  <div class="quote-box" style="left:248px;top:100px;width:112px;box-shadow:0 2px 4px rgba(0,0,0,.15)">Short exercises help teams turn new ideas into habits that last.</div>
  <div class="quote-box" style="left:108px;top:168px;width:110px;box-shadow:0 2px 4px rgba(0,0,0,.1)">Short exercises help teams turn new ideas into habits that last.</div>
  <div class="quote-box" style="left:256px;top:168px;width:110px;box-shadow:0 2px 4px rgba(0,0,0,.1)">Short exercises help teams turn new ideas into habits that last.</div>
  <div class="foot-left">COPYRIGHT © 2020</div><div class="foot-right">PAGE | 20</div>
</section>

<section class="slide" style="left:800px;top:1840px;background:linear-gradient(180deg,var(--gold),var(--orange))">
  <div class="break-title" style="top:156px">PRESENTATION SECTION BREAK</div>
  <div class="break-rule" style="left:0;right:150px;top:178px"></div>
  <div class="break-sub" style="top:172px">TITLE GOES HERE</div>
  <div class="break-url">www.marenholt.example</div>
</section>

<!-- Row 8 -->
<section class="slide" style="left:16px;top:2071px;background:var(--teal)">
  <div class="break-title" style="top:156px">PRESENTATION SECTION BREAK</div>
  <div class="break-rule" style="left:0;right:150px;top:178px"></div>
  <div class="break-sub" style="top:172px">TITLE GOES HERE</div>
  <div class="break-url">www.marenholt.example</div>
</section>

<section class="slide" style="left:408px;top:2071px;background:var(--plum)">
  <div class="break-title" style="top:156px">PRESENTATION SECTION BREAK</div>
  <div class="break-rule" style="left:0;right:150px;top:178px"></div>
  <div class="break-sub" style="top:172px">TITLE GOES HERE</div>
  <div class="break-url">www.marenholt.example</div>
</section>

<section class="slide" style="left:800px;top:2071px">
  <div class="brand mid" style="left:13px;top:64px">MAREN HOLT</div>
  <div class="serif abs" style="left:13px;top:86px;color:var(--teal);font-size:17px">PRESENTATION TITLE</div>
  <div class="abs" style="left:13px;top:108px;color:var(--teal);font-size:6px">SUB TITLE GOES HERE</div>
  <div class="abs" style="left:0;bottom:0;width:384px;height:24px;background:var(--teal)"></div>
</section>

</body>
</html>
```